Business Card Design for Cybersecurity Company - QuorvaNet Systems

We need a business card design for our new cybersecurity company, QuorvaNet. We’re going for a clean, hi tech look that feels modern, premium, and trustworthy. We want a design that really stands out and makes people say WOW when we hand it over!

QuorvaNet delivers reliable IT support and managed services for small and mid sized businesses. We help companies stay secure, efficient, and connected through proactive monitoring, cybersecurity services, cloud management, and remote support.

Target Market(s)

Designers should target small and mid sized businesses that need dependable cybersecurity and IT support.

Industry/Entity Type

Cybersecurity, Managed Service Provider, IT services

Contact Information for Business Card

Contact information

Requirements
Must have
• The card should look clean, modern, and tech focused, with the QuorvaNet logo, clear contact info, and strong readability. It needs to feel premium and professional while still keeping a simple layout that fits a cybersecurity and IT brand.
Nice to have
• Nice to have elements include subtle touches that give the card a modern, tech feel, along with a layout that works well in different background styles.
Should not have
• The card should avoid clutter, loud graphics, or anything that takes attention away from the logo and contact details.

```html
<!DOCTYPE html>
<html lang="en">
<head>
<meta charset="utf-8">
<title>QuorvaNet Systems – Business Card</title>
<link rel="stylesheet" href="https://fonts.googleapis.com/css2?family=Poppins:wght@300;400&display=swap">
<style>
  :root {
    --page: #e4e4e4;
    --card: #030305;
    --brand: #5a46ee;
    --accent: #3d5ef2;
    --text: #f2f2f7;
    --deco-a: rgba(40, 40, 140, 0.45);
    --deco-b: rgba(70, 30, 150, 0.25);
    --deco-back: rgba(30, 36, 70, 0.35);
  }
  * { margin: 0; padding: 0; box-sizing: border-box; }
  html, body {
    width: 1200px; height: 1200px; overflow: hidden;
    background: var(--page);
    font-family: "Poppins", sans-serif;
  }
  .card {
    position: absolute; left: 200px;
    width: 800px; height: 457px;
    background: var(--card); overflow: hidden;
  }
  .card--front { top: 120px; }
  .card--back { top: 630px; }

  .deco { position: absolute; }
  .deco--top-right {
    left: 470px; top: 0; width: 330px; height: 165px;
    background: radial-gradient(ellipse at 55% 30%, var(--deco-a), var(--deco-b) 45%, transparent 75%);
  }
  .deco--bottom-left {
    left: 0; top: 280px; width: 360px; height: 177px;
    background: radial-gradient(ellipse at 45% 85%, var(--deco-a), transparent 72%);
  }
  .deco--back-field {
    left: 100px; top: 0; width: 600px; height: 457px;
    background: radial-gradient(ellipse at 50% 55%, var(--deco-back), transparent 70%);
  }

  .wordmark {
    position: absolute; display: flex; align-items: center; gap: 14px;
    color: var(--brand); font-weight: 400;
  }
  .wordmark__dot {
    width: 22px; height: 22px; border-radius: 50%; background: var(--brand); flex: none;
  }
  .wordmark__text { line-height: 1; }
  .wordmark__name { display: block; font-size: 40px; letter-spacing: 0.5px; }
  .wordmark__sub { display: block; font-size: 17px; letter-spacing: 9px; margin-top: 8px; }

  .card--front .wordmark { left: 62px; top: 103px; }
  .card--back .wordmark { left: 50%; top: 182px; transform: translateX(-50%); }
  .card--back .wordmark__name { font-size: 50px; }
  .card--back .wordmark__sub { font-size: 20px; letter-spacing: 11px; margin-top: 10px; }
  .card--back .wordmark__dot { width: 26px; height: 26px; }

  .person {
    position: absolute; right: 68px; top: 198px; text-align: right;
  }
  .person__name { color: var(--brand); font-size: 33px; font-weight: 300; line-height: 1.1; }
  .person__role { color: var(--text); font-size: 18px; font-weight: 300; margin-right: 10px; }

  .contacts {
    position: absolute; right: 76px; top: 284px; list-style: none; text-align: right;
  }
  .contacts li {
    color: var(--text); font-size: 20px; font-weight: 300; line-height: 25px;
    display: flex; justify-content: flex-end; align-items: center; gap: 10px;
  }
  .contacts svg { width: 18px; height: 18px; flex: none; }

  .tagline {
    position: absolute; left: 0; right: 0; top: 356px;
    text-align: center; color: var(--text);
    font-size: 19px; font-weight: 300; line-height: 23px;
  }
</style>
</head>
<body>

<section class="card card--front">
  <div class="deco deco--top-right" role="img" aria-label="Faint circuit-line hexagon decoration"></div>
  <div class="deco deco--bottom-left" role="img" aria-label="Faint circuit-line hexagon decoration"></div>

  <div class="wordmark">
    <span class="wordmark__dot"></span>
    <span class="wordmark__text">
      <span class="wordmark__name">QuorvaNet</span>
      <span class="wordmark__sub">Systems</span>
    </span>
  </div>

  <div class="person">
    <p class="person__name">Dylan Marsh</p>
    <p class="person__role">Owner | CEO</p>
  </div>

  <ul class="contacts">
    <li>(855) 480-7731
      <svg viewBox="0 0 24 24"><path fill="#3d5ef2" d="M6.6 10.8a15 15 0 0 0 6.6 6.6l2.2-2.2c.3-.3.7-.4 1-.2 1.1.4 2.3.6 3.6.6.6 0 1 .4 1 1V20c0 .6-.4 1-1 1C10.6 21 3 13.4 3 4c0-.6.4-1 1-1h3.5c.6 0 1 .4 1 1 0 1.3.2 2.5.6 3.6.1.3 0 .7-.2 1z"/></svg>
    </li>
    <li>(813) 555-0192
      <svg viewBox="0 0 24 24"><rect x="6" y="2" width="12" height="20" rx="2" fill="none" stroke="#3d5ef2" stroke-width="2.4"/><rect x="10" y="17.5" width="4" height="1.5" fill="#3d5ef2"/></svg>
    </li>
    <li>dylan@quorvanet.com
      <svg viewBox="0 0 24 24"><rect x="2" y="5" width="20" height="14" rx="1" fill="#3d5ef2"/><path d="M3 6l9 7 9-7" fill="none" stroke="#030305" stroke-width="1.6"/></svg>
    </li>
    <li>www.quorvanet.com
      <svg viewBox="0 0 24 24"><circle cx="12" cy="12" r="10" fill="#3d5ef2"/><path d="M2 12h20M12 2c3 3 3 17 0 20M12 2c-3 3-3 17 0 20" fill="none" stroke="#030305" stroke-width="1.4"/></svg>
    </li>
  </ul>
</section>

<section class="card card--back">
  <div class="deco deco--back-field" role="img" aria-label="Large faint circuit hexagon decoration"></div>

  <div class="wordmark">
    <span class="wordmark__dot"></span>
    <span class="wordmark__text">
      <span class="wordmark__name">QuorvaNet</span>
      <span class="wordmark__sub">Systems</span>
    </span>
  </div>

  <p class="tagline">proactive monitoring, cybersecurity services<br>cloud management, &amp; remote support.</p>
</section>

</body>
</html>
```